Need Stunning, Visual Tree Identification Booklet

We are looking for a magazine/booklet style design for tree and plant identification. They need to be organized according to tree/plant type and contain a picture and tree/plant information. I would like to see 4 trees/plants per page. I will be including links for all the information needed but you will be responsible for gathering pictures as we have none to provide. This is not a booklet that will be sold or given out, it is solely to be used by our company internally for training and for presenting during sales meetings.

Target Market(s)

To be used by our sales staff when meeting with customers and selling trees and plants.

Industry/Entity Type

Landscape Gardening

Font styles to use
Serif

Requirements
Must have
• Attractive design that makes it easy to read and visual the trees and plants shown in the booklet. Design must be done in Adobe Illustrator or Adobe InDesign. Every tree/plant must have a picture, description, common name, Botanical name, Height, Width, Growth Rate, Function, Hardiness and Water Use. Would like to fit 4 trees/plants per page. Attached is a category outline.
Nice to have
• Clean, professional look. Using greens, whites and blacks

```html
<!DOCTYPE html>
<html lang="en">
<head>
<meta charset="utf-8">
<title>Citrus Trees – Tree Identification Booklet</title>
<link rel="stylesheet" href="https://fonts.googleapis.com/css2?family=Playfair+Display:wght@800;900&family=Lora:ital,wght@0,400;0,700;1,400&display=swap">
<style>
  :root {
    --backdrop: #e9eaec;
    --paper: #ffffff;
    --ink: #1a1a1a;
    --ink-soft: #2b2b2b;
    --ink-muted: #555555;
    --brand-green: #2fa533;
    --band-black: #111111;
    --tab-grey: #dcdcdc;
    --tab-text: #f7f7f7;
    --lime-a: #5f9a3a;
    --lime-b: #9cc4e6;
    --orange-a: #e2852a;
    --orange-b: #4d7a2c;
    --tree-a: #f0a23a;
    --tree-b: #7fb5e4;
    --lemon-a: #f2d23c;
    --lemon-b: #5b8a34;
  }
  * { box-sizing: border-box; margin: 0; padding: 0; }
  html, body {
    width: 1200px;
    height: 892px;
    overflow: hidden;
    background: var(--backdrop);
    font-family: "Lora", serif;
    color: var(--ink);
  }
  .booklet-page {
    position: absolute;
    left: 275px;
    top: 10px;
    width: 650px;
    height: 872px;
    background: var(--paper);
    box-shadow: 0 2px 14px rgba(0,0,0,0.12);
    overflow: hidden;
  }
  .page-tab {
    position: absolute;
    right: 0;
    top: 0;
    width: 300px;
    height: 24px;
    background: var(--tab-grey);
    color: var(--tab-text);
    font-weight: 700;
    font-size: 11px;
    letter-spacing: 2px;
    text-align: right;
    padding: 5px 22px 0 0;
  }
  .section-header {
    position: absolute;
    left: 0;
    top: 36px;
    width: 100%;
  }
  .section-title {
    font-family: "Playfair Display", serif;
    font-weight: 900;
    font-size: 36px;
    padding-left: 40px;
    line-height: 1;
  }
  .title-rule {
    margin-top: 8px;
    height: 11px;
    width: 330px;
    background: var(--band-black);
  }
  .title-rule-accent {
    height: 4px;
    width: 330px;
    background: var(--brand-green);
  }
  .section-intro {
    position: absolute;
    left: 40px;
    top: 116px;
    width: 570px;
    font-size: 13px;
    line-height: 1.45;
    color: var(--ink-soft);
  }
  .plant-list {
    position: absolute;
    left: 40px;
    top: 196px;
    width: 570px;
  }
  .plant-entry {
    display: grid;
    grid-template-columns: 1fr 220px;
    gap: 20px;
    align-items: center;
    height: 160px;
    margin-bottom: 6px;
  }
  .plant-entry--photo-left {
    grid-template-columns: 220px 1fr;
  }
  .plant-entry--photo-left .plant-photo { order: -1; }
  .plant-name {
    font-weight: 700;
    font-size: 14px;
    line-height: 1.2;
    color: var(--ink);
  }
  .plant-botanical {
    font-style: italic;
    font-size: 11.5px;
    color: var(--brand-green);
    margin-bottom: 3px;
  }
  .plant-description {
    font-size: 11px;
    line-height: 1.38;
    color: var(--ink-soft);
  }
  .plant-specs {
    display: grid;
    grid-template-columns: repeat(3, auto);
    column-gap: 10px;
    row-gap: 1px;
    margin-top: 4px;
    padding-top: 3px;
    border-top: 1px solid var(--brand-green);
    font-size: 9.5px;
    line-height: 1.3;
    color: var(--ink-muted);
  }
  .plant-specs dt { display: inline; font-weight: 700; color: var(--ink); }
  .plant-specs dd { display: inline; margin-left: 3px; }
  .plant-photo {
    width: 220px;
    height: 140px;
  }
  .plant-photo--lime { background: linear-gradient(135deg, var(--lime-b), var(--lime-a) 60%); }
  .plant-photo--orange { background: radial-gradient(circle at 40% 50%, var(--orange-a), var(--orange-b) 85%); }
  .plant-photo--tree { background: radial-gradient(circle at 50% 55%, var(--tree-a), #6b9b3a 65%, var(--tree-b)); }
  .plant-photo--lemon { background: radial-gradient(circle at 50% 45%, var(--lemon-a), var(--lemon-b) 90%); }
</style>
</head>
<body>
  <article class="booklet-page">
    <div class="page-tab">PAGE 3</div>

    <header class="section-header">
      <h1 class="section-title">Citrus Trees</h1>
      <div class="title-rule"></div>
      <div class="title-rule-accent"></div>
    </header>

    <p class="section-intro">The lower deserts of Arizona are one the world's best climates for growing citrus. Warm days and cool nights in winter produce wonderful fruit and the desert climate allows the growing of trees organically without the use of pesticides.</p>

    <section class="plant-list">
      <div class="plant-entry">
        <div class="plant-text">
          <h2 class="plant-name">Bearss Lime</h2>
          <p class="plant-botanical">Citrus latifolia</p>
          <p class="plant-description">AKA Tahitian lime, Persian lime. Nearly-thornless, grows vigorously to medium-large. Hardy as lemon. Fruit medium sized, light yellow rind at full maturity, seedless flesh, acidic, juicy. October to December.</p>
          <dl class="plant-specs">
            <div><dt>Height</dt><dd>15–20 ft</dd></div>
            <div><dt>Width</dt><dd>15–20 ft</dd></div>
            <div><dt>Growth</dt><dd>Moderate</dd></div>
            <div><dt>Function</dt><dd>Fruit, screen</dd></div>
            <div><dt>Hardiness</dt><dd>30°F</dd></div>
            <div><dt>Water</dt><dd>Medium</dd></div>
          </dl>
        </div>
        <div class="plant-photo plant-photo--lime" role="img" aria-label="Green limes hanging on a lime tree against blue sky"></div>
      </div>

      <div class="plant-entry plant-entry--photo-left">
        <div class="plant-text">
          <h2 class="plant-name">Blood Orange</h2>
          <p class="plant-botanical">Citrus sinensis</p>
          <p class="plant-description">Tree large, vigorous, densely foliaged. Fruit medium-large, quite variable, mid season. Deep reddish-orange color, easy to peel. Flesh deep orange-colored and juicy, with a rich, sweet flavor. Harvest January to February.</p>
          <dl class="plant-specs">
            <div><dt>Height</dt><dd>20–25 ft</dd></div>
            <div><dt>Width</dt><dd>15–20 ft</dd></div>
            <div><dt>Growth</dt><dd>Moderate</dd></div>
            <div><dt>Function</dt><dd>Fruit, shade</dd></div>
            <div><dt>Hardiness</dt><dd>28°F</dd></div>
            <div><dt>Water</dt><dd>Medium</dd></div>
          </dl>
        </div>
        <div class="plant-photo plant-photo--orange" role="img" aria-label="Ripe oranges among green leaves"></div>
      </div>

      <div class="plant-entry">
        <div class="plant-text">
          <h2 class="plant-name">Mexican Lime</h2>
          <p class="plant-botanical">Citrus aurantiifolia</p>
          <p class="plant-description">AKA Tahitian lime, Persian lime. Nearly-thornless, grows vigorously to medium-large. Hardy as lemon. Fruit medium sized, light yellow rind at full maturity, seedless flesh, acidic, juicy. October to December.</p>
          <dl class="plant-specs">
            <div><dt>Height</dt><dd>12–15 ft</dd></div>
            <div><dt>Width</dt><dd>10–15 ft</dd></div>
            <div><dt>Growth</dt><dd>Fast</dd></div>
            <div><dt>Function</dt><dd>Fruit, accent</dd></div>
            <div><dt>Hardiness</dt><dd>32°F</dd></div>
            <div><dt>Water</dt><dd>Medium</dd></div>
          </dl>
        </div>
        <div class="plant-photo plant-photo--tree" role="img" aria-label="Citrus tree laden with fruit under blue sky"></div>
      </div>

      <div class="plant-entry plant-entry--photo-left">
        <div class="plant-text">
          <h2 class="plant-name">Lisbon Lemon</h2>
          <p class="plant-botanical">Citrus limon</p>
          <p class="plant-description">Grows vigorously into large strong, upright but spreading trees. Fruit medium to large, flesh pale yellow, low-seeded, and very acidic. High productivity with several crops/year. Main crop winter and spring.</p>
          <dl class="plant-specs">
            <div><dt>Height</dt><dd>20–25 ft</dd></div>
            <div><dt>Width</dt><dd>20 ft</dd></div>
            <div><dt>Growth</dt><dd>Fast</dd></div>
            <div><dt>Function</dt><dd>Fruit, screen</dd></div>
            <div><dt>Hardiness</dt><dd>29°F</dd></div>
            <div><dt>Water</dt><dd>Medium</dd></div>
          </dl>
        </div>
        <div class="plant-photo plant-photo--lemon" role="img" aria-label="Yellow lemons on a leafy branch"></div>
      </div>
    </section>
  </article>
</body>
</html>
```